Birchwood Forage Business Cards

I need a business card with my logo, number, Facebook account, and some information about what I am selling. Green card with logo on the front. 847-302-1596 phone number, @birchwoodforage Facebook, •Orchardgrass Hay •Alfalfa Hay •Mixed Grass Hay , and “Premium Quality Hay” all written on the back.

Target Market(s)

Hay

Contact Information for Business Card

Phone number, Facebook, different types of hay.

Colors
00AB8E
00BBA5
67D7C9
C6EFE9
E9F9F6

```html
<!DOCTYPE html>
<html lang="en">
<head>
<meta charset="utf-8">
<title>Birchwood Forage Business Cards</title>
<link rel="stylesheet" href="https://fonts.googleapis.com/css2?family=Poppins:wght@400;500;600&family=Arimo:wght@700&family=Damion&display=swap">
<style>
  :root {
    --backdrop: #d9d4cc;
    --front-card: #cdeae6;
    --brand-green: #00a651;
    --ink: #231f20;
    --white: #ffffff;
    --band: #0b0b0b;
  }
  * { margin: 0; padding: 0; box-sizing: border-box; }
  html, body { width: 900px; height: 1200px; overflow: hidden; }
  body {
    position: relative;
    background: var(--backdrop);
    font-family: "Poppins", sans-serif;
  }
  .card {
    position: absolute;
    left: 82px;
    width: 733px;
    height: 428px;
    border-radius: 28px;
    overflow: hidden;
    box-shadow: 0 6px 14px rgba(0,0,0,0.25);
  }
  .card-front { top: 137px; background: var(--front-card); }
  .card-back { top: 634px; background: var(--brand-green); color: var(--white); }

  /* Front */
  .front-mark {
    position: absolute;
    left: 170px; top: 170px;
    width: 70px; height: 70px;
    border-radius: 50%;
    background: var(--brand-green);
  }
  .front-name {
    position: absolute;
    left: 262px; top: 170px;
    font-weight: 600;
    font-size: 34px;
    line-height: 1;
    color: var(--ink);
  }
  .front-phone {
    position: absolute;
    left: 320px; top: 228px;
    font-family: "Arimo", sans-serif;
    font-weight: 700;
    font-size: 37px;
    line-height: 1;
    color: var(--ink);
  }

  /* Back */
  .back-logo {
    position: absolute;
    left: 110px; top: 140px;
    width: 260px;
    text-align: center;
  }
  .back-mark {
    width: 64px; height: 64px;
    margin: 0 auto 14px;
    border-radius: 50%;
    background: var(--white);
  }
  .back-name { font-weight: 600; font-size: 26px; line-height: 1.1; }
  .divider {
    position: absolute;
    left: 368px; top: 118px;
    width: 2px; height: 170px;
    background: var(--white);
  }
  .contact { position: absolute; left: 395px; top: 152px; }
  .contact-name { font-weight: 500; font-size: 21px; line-height: 1.2; }
  .contact-role { font-size: 15px; line-height: 1.2; margin-bottom: 10px; }
  .contact-line {
    display: flex; align-items: center; gap: 8px;
    font-size: 16px; line-height: 1; margin-bottom: 6px;
  }
  .contact-line svg, .social-dot { width: 18px; height: 18px; flex: none; }
  .social-dot { border-radius: 50%; background: var(--white); }
  .tagline {
    position: absolute;
    left: 0; right: 0; top: 342px;
    text-align: center;
    font-family: "Damion", cursive;
    font-size: 24px;
    letter-spacing: 1px;
  }
  .product-band {
    position: absolute;
    left: 0; right: 0; bottom: 0;
    height: 37px;
    background: var(--band);
    display: flex; justify-content: center; align-items: center; gap: 10px;
    font-size: 15.5px; letter-spacing: 0.3px;
  }
  .band-dot { width: 8px; height: 8px; border-radius: 50%; background: var(--brand-green); }
</style>
</head>
<body>
  <section class="card card-front">
    <div class="front-mark"></div>
    <div class="front-name">Birchwood Forage</div>
    <div class="front-phone">847-302-1596</div>
  </section>

  <section class="card card-back">
    <div class="back-logo">
      <div class="back-mark"></div>
      <div class="back-name">Birchwood Forage</div>
    </div>
    <div class="divider"></div>
    <div class="contact">
      <div class="contact-name">Daniel Harper</div>
      <div class="contact-role">Owner</div>
      <div class="contact-line">
        <svg viewBox="0 0 18 18" aria-hidden="true">
          <circle cx="9" cy="9" r="9" fill="#fff"/>
          <path d="M6 4.5c.4-.3.9-.2 1.1.2l.9 1.6c.2.4.1.8-.2 1.1l-.6.5c.5 1.1 1.3 1.9 2.4 2.4l.5-.6c.3-.3.7-.4 1.1-.2l1.6.9c.4.2.5.7.2 1.1l-.6.8c-.4.5-1.1.7-1.7.5C8.3 12 6 9.7 5.2 7.2c-.2-.6 0-1.3.5-1.7z" fill="#00a651"/>
        </svg>
        <span>847-302-1596</span>
      </div>
      <div class="contact-line">
        <span class="social-dot"></span>
        <span>@birchwoodforage</span>
      </div>
    </div>
    <div class="tagline">Premium Quality Hay</div>
    <div class="product-band">
      <span>Orchardgrass Hay</span><span class="band-dot"></span>
      <span>Alfalfa Hay</span><span class="band-dot"></span>
      <span>Mixed Grass Hay</span>
    </div>
  </section>
</body>
</html>
```